BRANTWELL & BRANTWELL,LLP NEEDS A NEW LETTERHEAD DESIGN

a conservative yet contemporary layout befitting a long established
firm, consistent with the times, some form of logo so it catches ones attention, and is
admirable, but portrays integrity
Updates

I would like to approve #22066987 Please advise how to do this as it’s confusing on the site so I can approve payment for the designer

Target Market(s)

real estate investors and building management people

Industry/Entity Type

Law Firm

Font styles to use
Serif

Colors

Designer to choose colors to be used in the design.

Requirements
Must have
• some form of conservative logo

```html
<!DOCTYPE html>
<html lang="en">
<head>
<meta charset="utf-8">
<title>Brantwell &amp; Brantwell, LLP — Letterhead</title>
<link rel="stylesheet" href="https://fonts.googleapis.com/css2?family=Cinzel:wght@400&family=Marcellus&display=swap">
<style>
  :root {
    --backdrop: #d8cfcd;
    --paper: #ffffff;
    --ink: #2b2b2b;
    --ink-soft: #555555;
    --rule: #7a7a7a;
  }
  * { margin: 0; padding: 0; box-sizing: border-box; }
  html, body {
    width: 1200px;
    height: 784px;
    overflow: hidden;
    background: var(--backdrop);
  }
  .canvas {
    position: relative;
    width: 1200px;
    height: 784px;
    display: flex;
    align-items: center;
    justify-content: center;
  }
  .letterhead {
    position: relative;
    width: 520px;
    height: 736px;
    background: var(--paper);
    box-shadow: 0 2px 10px rgba(0,0,0,0.12);
    padding: 34px 40px 30px;
    display: flex;
    flex-direction: column;
  }
  .masthead {
    display: flex;
    flex-direction: column;
    align-items: flex-end;
  }
  .firm-name {
    font-family: 'Cinzel', serif;
    font-weight: 400;
    font-size: 22px;
    letter-spacing: 0.5px;
    color: var(--ink);
    white-space: nowrap;
  }
  .tagline-row {
    display: flex;
    align-items: center;
    width: 100%;
    gap: 10px;
    margin-top: 8px;
  }
  .tagline-row .rule {
    flex: 1;
    height: 1px;
    background: var(--rule);
  }
  .tagline-row .rule.short { flex: 0 0 46px; }
  .tagline {
    font-family: 'Marcellus', serif;
    font-size: 7.5px;
    letter-spacing: 0.6px;
    color: var(--ink-soft);
    white-space: nowrap;
  }
  .body-area { flex: 1; }
  .footer {
    display: flex;
    flex-direction: column;
    align-items: center;
  }
  .footer .rule {
    width: 100%;
    height: 1px;
    background: var(--rule);
    margin-bottom: 10px;
  }
  .contact-line {
    font-family: 'Marcellus', serif;
    font-size: 8px;
    letter-spacing: 0.3px;
    color: var(--ink-soft);
    white-space: nowrap;
    line-height: 1.7;
  }
</style>
</head>
<body>
  <div class="canvas">
    <div class="letterhead">
      <header class="masthead">
        <h1 class="firm-name">BRANTWELL &amp; BRANTWELL,LLP</h1>
        <div class="tagline-row">
          <span class="rule"></span>
          <span class="tagline">NEW YORK CITY LANDLORD / TENANT REAL ESTATE LAW</span>
          <span class="rule short"></span>
        </div>
      </header>
      <main class="body-area"></main>
      <footer class="footer">
        <span class="rule"></span>
        <p class="contact-line">P : +330 5550-0142 | M : +330 5550-0187 | E : INFO@BRANTWELLLAW.COM | W : WWW.BRANTWELLLAW.COM</p>
        <p class="contact-line">A : 2150 ELMCREST AVENUE NEW YORK, NY 10016</p>
      </footer>
    </div>
  </div>
</body>
</html>
```